Business Card Design

Business Card for professional consulting firm working with large financial institutions.

Target Market(s)

Executive buyers

Industry/Entity Type

Banking

Contact Information for Business Card

Mild creativity wanted. Not boring, but do elaborate artwork.

Font styles to use
Serif
Sans Serif

Colors

Designer to choose colors to be used in the design.

Requirements
Must have
• Standard business card features - company name, individual name, telephone, website, email, locations.
Nice to have
• Two colors
Should not have
• too many colors, fancy printing, cartoons.

```html
<!DOCTYPE html>
<html lang="en">
<head>
<meta charset="utf-8">
<title>Ardent Ledger – Business Card</title>
<link rel="stylesheet" href="https://fonts.googleapis.com/css2?family=Exo+2:wght@300;400;500&display=swap">
<style>
  :root {
    --navy: #1f3447;
    --navy-deep: #10222f;
    --mist: #e4eeee;
    --paper: #ffffff;
    --ink: #1f3447;
  }
  * { margin: 0; padding: 0; box-sizing: border-box; }
  html, body { width: 686px; height: 1200px; overflow: hidden; background: var(--paper); }
  .card {
    position: relative; width: 686px; height: 1200px; background: var(--paper);
    font-family: "Exo 2", sans-serif; color: var(--ink); overflow: hidden;
  }
  .side-band { position: absolute; left: 42px; top: 0; width: 108px; height: 1200px; background: var(--navy); }
  .name-plate {
    position: absolute; left: 265px; top: 120px; width: 421px; height: 117px;
    background: var(--navy); color: var(--paper); padding: 14px 0 0 17px;
  }
  .person-name { font-size: 46px; line-height: 52px; font-weight: 300; letter-spacing: 0.3px; }
  .person-name .first { font-weight: 500; }
  .person-role { font-size: 28px; line-height: 34px; font-weight: 300; margin-top: 0; }
  .company-name {
    position: absolute; left: 183px; width: 424px; top: 440px; text-align: center;
    font-family: "Exo 2", sans-serif; font-size: 44px; line-height: 60px;
    font-weight: 300; letter-spacing: 1px; color: var(--navy);
  }
  .tagline {
    position: absolute; left: 219px; top: 574px; white-space: nowrap;
    font-size: 28px; line-height: 36px; font-weight: 300; color: var(--navy);
  }
  .contact-row { position: absolute; left: 42px; width: 644px; height: 95px; display: flex; }
  .contact-row .icon {
    width: 108px; height: 100%; background: var(--navy-deep);
    display: flex; align-items: center; justify-content: center;
  }
  .contact-row .details {
    flex: 1; background: var(--mist); padding-left: 35px;
    display: flex; flex-direction: column; justify-content: center;
    font-size: 27px; line-height: 34px; font-weight: 300; color: var(--navy);
  }
  .row-address { top: 681px; }
  .row-phone { top: 797px; }
  .row-email { top: 911px; }
  .row-web { top: 1027px; }
</style>
</head>
<body>
<div class="card">
  <div class="side-band"></div>

  <div class="name-plate">
    <div class="person-name"><span class="first">Connor</span> Hale</div>
    <div class="person-role">Individual Position</div>
  </div>

  <div class="company-name">Ardent Ledger</div>
  <div class="tagline">professional consulting firm</div>

  <div class="contact-row row-address">
    <div class="icon">
      <svg width="40" height="40" viewBox="0 0 40 40" aria-hidden="true">
        <path d="M2 8 L13 3 L27 8 L38 3 L38 32 L27 37 L13 32 L2 37 Z" fill="#fff"/>
        <path d="M13 3 V32 M27 8 V37" stroke="#10222f" stroke-width="2"/>
      </svg>
    </div>
    <div class="details"><span>123, Your Street, Your City,</span><span>Here type Your Country</span></div>
  </div>

  <div class="contact-row row-phone">
    <div class="icon">
      <svg width="38" height="38" viewBox="0 0 38 38" aria-hidden="true">
        <rect x="1" y="1" width="36" height="36" rx="7" fill="#fff"/>
        <path d="M11 8 C9 10 8 13 11 19 C14 25 19 29 24 30 C27 30 29 28 30 26 L26 22 L23 24 C20 23 16 19 15 16 L17 13 Z" fill="#10222f"/>
      </svg>
    </div>
    <div class="details"><span>+000 - 1234 - 5567</span><span>+000 - 7869 - 5567</span></div>
  </div>

  <div class="contact-row row-email">
    <div class="icon">
      <svg width="40" height="28" viewBox="0 0 40 28" aria-hidden="true">
        <rect x="0" y="0" width="40" height="28" rx="3" fill="#fff"/>
        <path d="M2 3 L20 16 L38 3" fill="none" stroke="#10222f" stroke-width="2.5"/>
      </svg>
    </div>
    <div class="details"><span>ardentledger@mailbox.com</span><span>info@ardentledger.com</span></div>
  </div>

  <div class="contact-row row-web">
    <div class="icon">
      <svg width="38" height="38" viewBox="0 0 38 38" aria-hidden="true">
        <circle cx="19" cy="19" r="18" fill="#fff"/>
        <ellipse cx="19" cy="19" rx="7" ry="18" fill="none" stroke="#10222f" stroke-width="2"/>
        <path d="M1 19 H37 M4 10 H34 M4 28 H34" stroke="#10222f" stroke-width="2"/>
      </svg>
    </div>
    <div class="details"><span>www.ardentledger.com</span></div>
  </div>
</div>
</body>
</html>
```